Red Sea Boat trips in need of Business Card for Private Boat Tours

We need a Business card for a new business set-up in Egypt on the Red Sea for private snorkelling and boat excursions to one of the world's most beautiful reefs. We have wording logo already set-up which matches the boat but we need business cards to be bright and colourful with pictures of boat

Industry/Entity Type

Tourism

Contact Information for Business Card

Two Silver Herons (font provided) Boat Trips

```html
<!DOCTYPE html>
<html lang="en">
<head>
<meta charset="utf-8">
<title>Two Silver Herons – Business Card</title>
<link href="https://fonts.googleapis.com/css2?family=Arimo:wght@400;700&display=swap" rel="stylesheet">
<style>
  :root {
    --page: #e9e4dc;
    --front-deep: #050505;
    --front-reef: #3a3a36;
    --front-fish: #b9a623;
    --brand-yellow: #f2e600;
    --sky-top: #5f97d6;
    --sky-low: #a9c6e6;
    --sea: #2fb6cf;
    --sea-deep: #1f8fae;
    --ink: #111417;
    --shadow: rgba(0,0,0,0.35);
  }
  * { box-sizing: border-box; margin: 0; padding: 0; }
  html, body { width: 1200px; height: 900px; overflow: hidden; }
  body {
    background: var(--page);
    font-family: "Arimo", Arial, sans-serif;
    position: relative;
  }
  .card {
    position: absolute;
    left: 300px;
    width: 600px;
    height: 343px;
    overflow: hidden;
    box-shadow: 0 10px 24px var(--shadow);
  }
  .card--front { top: 70px; }
  .card--back { top: 470px; }

  .photo { position: absolute; inset: 0; }
  .photo--reef {
    background:
      radial-gradient(ellipse 22% 26% at 48% 48%, var(--front-fish) 0%, rgba(185,166,35,0.35) 55%, transparent 100%),
      radial-gradient(ellipse 60% 55% at 62% 35%, var(--front-reef) 0%, transparent 75%),
      var(--front-deep);
  }
  .photo--harbour {
    background:
      linear-gradient(180deg, var(--sky-top) 0%, var(--sky-low) 48%, var(--sea) 56%, var(--sea-deep) 100%);
  }

  .brand-name {
    position: absolute;
    font-weight: 700;
    white-space: nowrap;
  }
  .card--front .brand-name {
    color: var(--brand-yellow);
    font-size: 40px;
    right: 70px;
    bottom: 40px;
  }
  .card--back .brand-name {
    color: var(--ink);
    font-size: 34px;
    right: 28px;
    top: 26px;
  }

  .address {
    position: absolute;
    right: 28px;
    top: 80px;
    text-align: right;
    font-size: 14px;
    line-height: 1.3;
    color: var(--ink);
  }

  .person {
    position: absolute;
    left: 32px;
    top: 120px;
    color: var(--ink);
  }
  .person__name { font-size: 22px; font-weight: 700; letter-spacing: 0.5px; }
  .person__role { font-size: 15px; margin-top: 2px; }

  .contact {
    position: absolute;
    left: 44px;
    top: 190px;
    list-style: none;
    font-size: 15px;
    color: var(--ink);
  }
  .contact__item {
    display: flex;
    align-items: center;
    gap: 9px;
    height: 24px;
  }
  .contact__icon { width: 15px; height: 15px; flex: none; }
</style>
</head>
<body>

  <section class="card card--front">
    <div class="photo photo--reef" role="img" aria-label="Photo of a yellow reef fish swimming in front of dark coral"></div>
    <div class="brand-name">Two Silver Herons</div>
  </section>

  <section class="card card--back">
    <div class="photo photo--harbour" role="img" aria-label="Photo of a white motor boat with a navy canopy moored in turquoise Red Sea water under a blue sky"></div>
    <div class="brand-name">Two Silver Herons</div>
    <p class="address">00 dummy city<br>dummy place 0000</p>

    <div class="person">
      <div class="person__name">JOHN SMITH</div>
      <div class="person__role">Director</div>
    </div>

    <ul class="contact">
      <li class="contact__item">
        <svg class="contact__icon" viewBox="0 0 16 16" aria-hidden="true">
          <path d="M3.5 1.5l2.5 3-1.5 1.6c.8 1.8 2.2 3.2 4 4l1.6-1.5 3 2.5-1.4 2.4C6.9 13.3 2.7 9.1 1.2 3z" fill="var(--ink)"/>
        </svg>
        <span>300-200-9000</span>
      </li>
      <li class="contact__item">
        <svg class="contact__icon" viewBox="0 0 16 16" aria-hidden="true">
          <rect x="1" y="3.5" width="14" height="9" fill="var(--ink)"/>
          <path d="M1.5 4l6.5 5 6.5-5" fill="none" stroke="var(--sky-low)" stroke-width="1.2"/>
        </svg>
        <span>info@twosilverherons.com</span>
      </li>
      <li class="contact__item">
        <svg class="contact__icon" viewBox="0 0 16 16" aria-hidden="true" fill="none" stroke="var(--ink)" stroke-width="1.2">
          <circle cx="8" cy="8" r="6.5"/>
          <ellipse cx="8" cy="8" rx="3" ry="6.5"/>
          <path d="M1.5 8h13M2.5 4.8h11M2.5 11.2h11"/>
        </svg>
        <span>www.twosilverherons.com</span>
      </li>
    </ul>
  </section>

</body>
</html>
```